Window Treatment specialists need business card design

We are moving into a new location and want to highlight our expertise and all we have to offer. We are now a Marlowe Tenney Gallery for customized window treatments. We also offer custom soft treatments i.e drapery, valances, cornices, upholstery, pillows, color design services, outdoor fabrics, and specialize in motorization of hard treatments.

Target Market(s)

Home Owners 30- 55 with annual income $150,000 and up

Industry/Entity Type

Home Improvement

Contact Information for Business Card

We want our location, name, email, website, phone number, fax, business logo, and Marlowe Tenney logo on the card. Anything else we are open to the design.

Font styles to use
Sans Serif

Requirements
Must have
• location, name, email, website, phone number, fax, business logo, and Marlowe Tenney logo on the card. Anything else we are open to the design.

```html
<!DOCTYPE html>
<html lang="en">
<head>
<meta charset="utf-8">
<title>Larkfield Interiors – Business Card</title>
<link rel="stylesheet" href="https://fonts.googleapis.com/css2?family=Open+Sans:wght@400;600;700&display=swap">
<style>
  :root {
    --page-bg: #e9e8e6;
    --card-white: #ffffff;
    --brand-teal: #a2cacd;
    --logo-teal: #9cc7ca;
    --band-grey: #3d3d3d;
    --ink: #1c1c1c;
  }
  * { margin: 0; padding: 0; box-sizing: border-box; }
  html, body { width: 1200px; height: 900px; overflow: hidden; }
  body {
    background: var(--page-bg);
    font-family: "Open Sans", Arial, sans-serif;
    color: var(--ink);
    position: relative;
  }
  .card {
    position: absolute;
    background: var(--card-white);
    overflow: hidden;
    box-shadow: 0 2px 8px rgba(0,0,0,0.12);
  }
  .card-front { left: 77px; top: 35px; width: 588px; height: 363px; }
  .card-back  { left: 388px; top: 505px; width: 567px; height: 352px; }
  .card-bands { position: absolute; inset: 0; width: 100%; height: 100%; }
  .band-teal { fill: var(--brand-teal); }
  .band-grey { fill: var(--band-grey); }

  .brand-name {
    position: absolute;
    color: var(--logo-teal);
    font-weight: 400;
    text-align: center;
    text-transform: lowercase;
    line-height: 1;
  }
  .card-front .brand-name { left: 120px; width: 350px; top: 62px; font-size: 40px; }
  .card-back  .brand-name { left: 83px; width: 400px; top: 38px; font-size: 44px; }
  .brand-name span { display: block; }
  .brand-name span + span { margin-top: 6px; }

  .person {
    position: absolute; right: 315px; top: 260px; text-align: right;
  }
  .person-name { font-size: 20px; font-weight: 700; line-height: 1.2; }
  .person-role { font-size: 15px; font-weight: 400; line-height: 1.4; }

  .contact-list {
    position: absolute; left: 294px; top: 249px; list-style: none;
  }
  .contact-list li {
    display: flex; align-items: center; height: 21px;
    font-size: 15px;
  }
  .contact-icon { width: 12px; height: 12px; margin-right: 13px; fill: var(--ink); }

  .address {
    position: absolute; left: 0; width: 576px; top: 327px;
    text-align: center; font-size: 15px;
  }

  .services {
    position: absolute; left: 0; width: 567px; top: 181px; text-align: center;
  }
  .services-title {
    font-size: 19px; font-weight: 700; text-decoration: underline;
    text-underline-offset: 3px; margin-bottom: 6px; line-height: 1.3;
  }
  .services-line {
    font-size: 15px; font-weight: 600; height: 32px; line-height: 32px;
    display: flex; justify-content: center; align-items: center;
  }
  .bullet { width: 11px; height: 11px; margin: 0 8px; fill: var(--ink); }
</style>
</head>
<body>

<section class="card card-front" aria-label="Business card front">
  <svg class="card-bands" viewBox="0 0 588 363" preserveAspectRatio="none" aria-hidden="true">
    <polygon class="band-grey" points="0,198 403,198 383,224 0,224"/>
    <polygon class="band-teal" points="0,228 385,228 415,190 588,190 588,363 0,363"/>
  </svg>
  <div class="brand-name"><span>larkfield</span><span>interiors</span></div>

  <div class="person">
    <p class="person-name">Elliot Marsh</p>
    <p class="person-role">Managing Director</p>
  </div>

  <ul class="contact-list">
    <li>
      <svg class="contact-icon" viewBox="0 0 24 24" aria-hidden="true"><path d="M6.6 10.8a15.1 15.1 0 0 0 6.6 6.6l2.2-2.2a1 1 0 0 1 1-.25 11.4 11.4 0 0 0 3.6.57 1 1 0 0 1 1 1V20a1 1 0 0 1-1 1A17 17 0 0 1 3 4a1 1 0 0 1 1-1h3.5a1 1 0 0 1 1 1c0 1.25.2 2.45.57 3.57a1 1 0 0 1-.25 1z"/></svg>
      044-555 018 246
    </li>
    <li>
      <svg class="contact-icon" viewBox="0 0 24 24" aria-hidden="true"><path d="M3 5h18v14H3z M3 5l9 7 9-7" fill="none" stroke="#1c1c1c" stroke-width="0"/><path d="M3 6v13h18V6l-9 7z M4 5l8 6 8-6z"/></svg>
      info@larkfieldinteriors.com
    </li>
    <li>
      <svg class="contact-icon" viewBox="0 0 24 24" aria-hidden="true"><circle cx="12" cy="12" r="9" fill="none" stroke="#1c1c1c" stroke-width="2"/><path d="M3 12h18M12 3c-3 3-3 15 0 18M12 3c3 3 3 15 0 18" fill="none" stroke="#1c1c1c" stroke-width="1.6"/></svg>
      www.larkfieldinteriors.com
    </li>
  </ul>

  <p class="address">48 Willow Lane, Brookhaven Township, 20417.</p>
</section>

<section class="card card-back" aria-label="Business card back">
  <svg class="card-bands" viewBox="0 0 567 352" preserveAspectRatio="none" aria-hidden="true">
    <polygon class="band-grey" points="0,149 402,149 382,174 0,174"/>
    <polygon class="band-teal" points="0,177 384,177 410,141 567,141 567,352 0,352"/>
  </svg>
  <div class="brand-name"><span>larkfield</span><span>interiors</span></div>

  <div class="services">
    <p class="services-title">Custom soft treatments</p>
    <p class="services-line">Drapery
      <svg class="bullet" viewBox="0 0 12 12" aria-hidden="true"><circle cx="6" cy="2.8" r="2.6"/><circle cx="6" cy="9.2" r="2.6"/><circle cx="2.8" cy="6" r="2.6"/><circle cx="9.2" cy="6" r="2.6"/></svg>
      Valances</p>
    <p class="services-line">Cornices
      <svg class="bullet" viewBox="0 0 12 12" aria-hidden="true"><circle cx="6" cy="2.8" r="2.6"/><circle cx="6" cy="9.2" r="2.6"/><circle cx="2.8" cy="6" r="2.6"/><circle cx="9.2" cy="6" r="2.6"/></svg>
      Upholstery
      <svg class="bullet" viewBox="0 0 12 12" aria-hidden="true"><circle cx="6" cy="2.8" r="2.6"/><circle cx="6" cy="9.2" r="2.6"/><circle cx="2.8" cy="6" r="2.6"/><circle cx="9.2" cy="6" r="2.6"/></svg>
      Pillows</p>
    <p class="services-line">Color Design Services
      <svg class="bullet" viewBox="0 0 12 12" aria-hidden="true"><circle cx="6" cy="2.8" r="2.6"/><circle cx="6" cy="9.2" r="2.6"/><circle cx="2.8" cy="6" r="2.6"/><circle cx="9.2" cy="6" r="2.6"/></svg>
      Outdoor fabrics</p>
    <p class="services-line">and Specialize in motorization of hard treatments</p>
  </div>
</section>

</body>
</html>
```